Blogging Platform for Christian Missions

We need the main (one) page design for FaithPostly. FaithPostly is a blogging platform for people (missionaries) who work for Christian Mission organisations in various countries. It will provides an easy way for them to setup and maintain a blog that will have features specifically for missions.

There's a lot of work involved in creating a web page design so I am happy to receive many quick rough designs. I will select my favourite four or five designs and these can submit the full design.

Please see the attached wireframe. Please also see the attached logo.

Main colours
- black
- white
- grey
- red (see logo colour) can be used occasionally eg. titles
- another complementary colour - occasionally used

Photos uploaded by the missionaries will provide colour for the website.

It needs to be a clean design that is not cluttered. The main focus are the blog posts. The information on the side complements the blog. There are navigational options at the top and bottom. The FaithPostly logo is not the main focus. The person's name (blog owner) is what needs to be most prominent.

I love the BrightNoma design (http://www.brightnoma-demo.net/). I particularly like the soft design - light grey background, white background boxes for content. The focus is the content - text and photos. I also like the subtle use of breakout image - "Step into the Venture". I like the black navigation header and the black footer. I do not want a exact copy of the site but I'd like to use this concept .

I also like this Quibbly design (http://calm.quibbly-demo.net/theme/preview/5193) because of the white box (and the shadow) for the content. I also like how the word "Quote" and the number of "notes" breaks out of the white content area (see attachment). I'd like to do this, if possible with the date. This is just a "nice to have" - definitely not essential. I don't like the font for the title in this example.

We have build a simple prototype already. I cautiously show this because I want the the design of this to be completely ignored. I used a free template. Along with the wireframe this prototype should an idea of what kind of content will be displayed but please don't look too much at it.
http://faithpostly-demo.org/blog/1

The design will be used to create a website using Verdant. We will use zScript so feel free to suggest an animation or lightbox effect to make your design more dynamic. This is a nice to have.

Once we have our final design we will need to define the style for:
- h1 through h4 tags
- Paragraphs
- Lists
- Block quotes
- Italics, bolding and underlining
- Links, including active, hover and visited states

Please let me know what additional information you need. Also let me know if there is something I have not considered.

Target Market(s)

The target customers are mission workers aged 25-35 who will post blog entries. These posts will be read by their friends and family.

Requirements
Must have
• Clean simple design. Must be inspired by the BrightNoma (http://www.brightnoma-demo.net/) design without copying it.
Nice to have
• Design element that breaks out of the boxes. See the screenshot attached from the Quibbly site. Described more in the project overview.
Should not have
• Should not use fonts that are not web-friendly. Should not have features that will be difficult to implement using HTML/CSS.

```html
<!DOCTYPE html>
<html lang="en">
<head>
<meta charset="utf-8">
<title>FaithPostly – Hannah Price</title>
<link href="https://fonts.googleapis.com/css2?family=Questrial&display=swap" rel="stylesheet">
<style>
:root{
  --ink:#1b1b1b;
  --bar:#111;
  --page:#ebebeb;
  --card:#fff;
  --panel:#eeeeee;
  --text:#333;
  --muted:#777;
  --red:#d0142a;
  --tab:#e8474f;
  --line:#bdbdbd;
  --footer:#222;
}
*{box-sizing:border-box;margin:0;padding:0}
html,body{width:726px;height:1200px;overflow:hidden}
body{position:relative;background:var(--page);font-family:"Questrial",Arial,sans-serif;color:var(--text)}
.abs{position:absolute}
.topbar{left:0;top:0;width:726px;height:28px;background:var(--bar);color:#fff;font-size:10px}
.topbar nav{position:absolute;top:8px;display:flex;gap:22px}
.topbar .main-nav{left:45px}
.topbar .account-nav{right:45px;gap:10px}
.brand{left:45px;top:50px;display:flex;align-items:center;gap:8px;font-size:22px;color:#555}
.brand .dot{width:22px;height:22px;border-radius:50%;background:var(--red)}
.search{left:505px;top:58px;width:176px;height:20px;border-radius:10px;background:#fff;border:1px solid #ccc;font-size:9px;color:#aaa;padding:4px 0 0 22px}
.search svg{position:absolute;left:8px;top:5px}
.follow{left:547px;top:116px;width:135px;height:23px;border-radius:12px;background:#fff;border:1px solid #bbb;font-size:10px;color:#333;display:flex;align-items:center;justify-content:center;gap:5px}
.card{left:47px;width:387px;background:var(--card);box-shadow:0 1px 6px rgba(0,0,0,.25)}
.card h2{position:absolute;left:21px;font-weight:400;font-size:18px;color:var(--ink)}
.card .rule{position:absolute;left:21px;right:21px;border-top:1px dotted #999}
.date{left:21px;width:32px;background:var(--tab);color:#fff;text-align:center;font-size:7px;line-height:1.1;padding-top:4px;box-shadow:0 1px 3px rgba(0,0,0,.3)}
.date b{display:block;font-weight:400;font-size:16px}
.photo{left:21px;width:342px;background:linear-gradient(#5a8fd0 0 30%,#e8e4dc 30% 60%,#58803a 60%)}
.caption{background:#1a1a1a;color:#fff;font-size:9px;padding:11px 0 0 18px}
.excerpt{position:absolute;left:0;width:387px;background:var(--panel);padding:16px 26px 0 26px;font-size:9px;line-height:1.33;text-align:justify}
.excerpt p{text-indent:26px;margin-bottom:10px}
.readmore{position:absolute;right:26px;font-size:8px;text-decoration:underline;color:#333}
.share{position:absolute;left:0;width:387px;height:43px;display:flex;align-items:center;font-size:8px;letter-spacing:.3px;color:#333}
.share span{display:flex;align-items:center;gap:6px;padding:0 16px;height:22px;border-right:1px dotted #aaa}
.share span:last-child{border:none}
.share i{width:18px;height:18px;border-radius:50%;background:#3b5da0;display:inline-block}
.share i.chirp{background:#5e97c8}
.pager{left:130px;top:1003px;display:flex;align-items:center;gap:14px;font-size:9px}
.pager .pill{width:27px;height:20px;border-radius:10px;background:#999;color:#fff;display:flex;align-items:center;justify-content:center;font-size:7px}
.side{left:469px;width:213px}
.owner-name{top:147px;right:44px;font-size:20px;color:var(--red);text-align:right}
.owner-org{top:170px;right:44px;font-size:12px;color:#444}
.portrait{left:469px;top:201px;width:108px;height:80px;background:linear-gradient(135deg,#8a5a3a,#c9a487 60%,#3d3020);border:1px solid #999}
.side-text{font-size:8.5px;line-height:1.33;text-align:justify;color:#333}
.side h3{font-weight:400;font-size:14px;color:#333;text-align:right}
.side .rule{border-top:1px dotted #999}
.side .more{font-size:8px;text-decoration:underline;text-align:right;margin-top:6px}
.side ul{list-style:none;font-size:9px;text-align:right;line-height:1.35;margin-top:6px}
.map{left:469px;top:571px;width:213px;height:114px;background:linear-gradient(135deg,#e6dcb8,#cdd8b0 50%,#a9c6d8);border:1px solid #aaa}
.footer{left:0;top:1056px;width:726px;height:144px;background:var(--footer);color:#ddd}
.footer h4{font-weight:400;font-size:9px;color:#fff;margin-bottom:10px}
.footer ul{list-style:none;font-size:8.5px;line-height:1.4;color:#ccc}
.footer .col{position:absolute;top:15px}
.footer .brand-mark{position:absolute;right:45px;top:92px;display:flex;align-items:center;gap:7px;font-size:18px;color:#bbb}
.footer .brand-mark .dot{width:20px;height:20px;border-radius:50%;background:var(--red)}
</style>
</head>
<body>
<header class="abs topbar">
  <nav class="main-nav"><span>Mission Blogs</span><span>Opportunities</span><span>Option3</span><span>Option4</span></nav>
  <nav class="account-nav"><span>Sign in</span><span>|</span><span>Register</span></nav>
</header>

<div class="abs brand"><span class="dot"></span><span>FaithPostly</span></div>
<div class="abs search"><svg width="9" height="9" viewBox="0 0 10 10"><circle cx="4" cy="4" r="3" fill="none" stroke="#999" stroke-width="1.3"/><line x1="6.3" y1="6.3" x2="9" y2="9" stroke="#999" stroke-width="1.3"/></svg>Search...</div>

<div class="abs follow"><svg width="10" height="10" viewBox="0 0 10 10"><rect x="0.5" y="0.5" width="9" height="9" fill="none" stroke="#666"/><path d="M5 2v6M2 5h6" stroke="#666" stroke-width="1.4"/></svg>Follow Hannah Price</div>

<!-- Post 1 -->
<article class="abs card" style="top:135px;height:543px">
  <h2 style="top:12px">Just Arrived</h2>
  <div class="rule" style="top:46px"></div>
  <div class="abs photo" role="img" aria-label="Photo of a two-storey white house with a green lawn" style="top:59px;height:256px"></div>
  <div class="abs caption" style="left:21px;top:265px;width:139px;height:34px">Photo of My New Home</div>
  <div class="excerpt" style="top:319px;height:181px">
    <p>Lorem ipsum dolor sit amet, consectetur adipisicing elit, sed do eiusmod tempor incididunt ut labore et dolore magna aliqua. Ut enim ad minim veniam, quis nostrud exercitation ullamco laboris nisi ut aliquip ex ea commodo consequat. Duis aute irure dolor in reprehenderit in voluptate velit esse cillum dolore eu fugiat nulla pariatur. Excepteur sint occaecat cupidatat non proident, sunt in culpa qui officia deserunt mollit anim id est laborum.</p>
    <p>Lorem ipsum dolor sit amet, consectetur adipisicing elit, sed do eiusmod tempor incididunt ut labore et dolore magna aliqua. Ut enim ad</p>
    <span class="readmore" style="top:163px">Read More</span>
  </div>
  <div class="share" style="top:500px"><span><i></i>SHARE ON FRIENDLINK</span><span><i class="chirp"></i>CHIRP THIS</span><span>3 COMMENTS</span></div>
</article>
<div class="abs date" style="top:153px;height:57px"><b>24</b>June<br>2011</div>

<!-- Post 2 -->
<article class="abs card" style="top:702px;height:279px">
  <h2 style="top:14px">Only 14 days to go before I fly for Malawi</h2>
  <div class="rule" style="top:45px"></div>
  <div class="excerpt" style="top:62px;height:174px">
    <p>Lorem ipsum dolor sit amet, consectetur adipisicing elit, sed do eiusmod tempor incididunt ut labore et dolore magna aliqua. Ut enim ad minim veniam, quis nostrud exercitation ullamco laboris nisi ut aliquip ex ea commodo consequat. Duis aute irure dolor in reprehenderit in voluptate velit esse cillum dolore eu fugiat nulla pariatur. Excepteur sint occaecat cupidatat non proident, sunt in culpa qui officia deserunt mollit anim id est laborum.</p>
    <p>Lorem ipsum dolor sit amet, consectetur adipisicing elit, sed do eiusmod tempor incididunt ut labore et dolore magna aliqua. Ut enim ad</p>
    <span class="readmore" style="top:156px">Read More</span>
  </div>
  <div class="share" style="top:236px"><span><i></i>SHARE ON FRIENDLINK</span><span><i class="chirp"></i>CHIRP THIS</span><span>3 COMMENTS</span></div>
</article>
<div class="abs date" style="top:726px;height:54px"><b>30</b>Mar<br>2011</div>

<nav class="abs pager"><span class="pill">Prev</span><span>1</span><span>2</span><span>3</span><span>4</span><span>5</span><span class="pill">Next</span></nav>

<!-- Sidebar -->
<div class="abs owner-name">Hannah Price</div>
<div class="abs owner-org">Kairo Mission Australia</div>
<div class="abs portrait" role="img" aria-label="Portrait photo of the blog owner"></div>
<div class="abs side side-text" style="top:201px;left:585px;width:97px">Lorem ipsum dolor sit amet, consectetur adipisicing elit, sed do eiusmod tempor incididunt ut labore et dolore magna aliqua. Ut</div>
<div class="abs side" style="top:285px">
  <p class="side-text">veniam, quis nostrud exercitation ullamco laboris nisi ut aliquip ex ea commodo consequat. Duis aute irure dolor in reprehenderit in voluptate velit esse cillum dolore eu fugiat nulla pariatur. Excepteur sint occaecat cupidatat non proident, sunt in culpa qui officia deserunt mollit anim id est laborum.</p>
  <p class="more">Read More</p>
</div>
<div class="abs side" style="top:390px">
  <div class="rule"></div>
  <h3 style="margin-top:14px">About Hannah's Ministry</h3>
  <p class="side-text" style="margin-top:6px">Veniam, quis nostrud exercitation ullamco laboris nisi ut aliquip ex ea commodo consequat. Duis aute irure dolor in reprehenderit in voluptate velit esse cillum dolore eu fugiat nulla pariatur. Excepteur sint occaecat cupidatat non proident, sunt in culpa qui officia deserunt mollit anim id est laborum.</p>
  <p class="more">Read More</p>
</div>
<div class="abs side" style="top:533px">
  <div class="rule"></div>
  <h3 style="margin-top:11px">About Malawi</h3>
</div>
<div class="abs map" role="img" aria-label="Road map of Malawi and surrounding region"></div>
<div class="abs side" style="top:692px">
  <p class="side-text">Veniam, quis nostrud exercitation ullamco laboris nisi ut aliquip ex ea commodo consequat. Duis aute irure dolor in reprehenderit in voluptate velit esse cillum dolore eu fugiat nulla pariatur.</p>
  <p class="more" style="margin-top:12px">Read More</p>
</div>
<div class="abs side" style="top:783px">
  <div class="rule"></div>
  <h3 style="margin-top:10px">Kairo Events</h3>
  <ul><li>Kairo Prayer Event - May 15th</li><li>Kairo Conference - June 30th</li></ul>
  <p class="more">Read More</p>
</div>
<div class="abs side" style="top:875px">
  <div class="rule"></div>
  <h3 style="margin-top:10px">Kairo Opportunities in Malawi</h3>
  <ul><li>Teacher in Blantyre (2yrs)</li><li>Financial Controller (long term)</li><li>Project Manager (6months)</li><li>Bible College Lecturer (long term)</li></ul>
  <p class="more">Read More</p>
</div>

<footer class="abs footer">
  <div class="col" style="left:20px"><h4>About Us</h4><ul><li>About FaithPostly</li><li>Missionaries</li><li>Mission Agencies</li><li>Churches</li><li>Mission Supporters</li><li>Privacy</li></ul></div>
  <div class="col" style="left:133px"><h4>Regions</h4><ul><li>Africa</li><li>Asia</li><li>North America</li><li>Latin America</li><li>Asia/Pacific</li></ul></div>
  <div class="col" style="left:227px"><h4>Mission Agencies</h4><ul><li>Harbor Mission</li><li>Global Bridge</li><li>Kairo Mission Australia</li><li>Wayfarer Fellowship</li></ul></div>
  <div class="brand-mark"><span class="dot"></span><span>FaithPostly</span></div>
</footer>
</body>
</html>
```